KVR Biz Cards

We are a property management company that manages luxury level residential estates. As such, we need a business card design that gives a high end feel. The idea at the moment is to list the services offered on the back of the card, and our company information on the front of the card.

Services for the back of the card are as follows:
Professional Property Management service, Home Hosting & Concierge Service, Holliday Home / Income Property Management

```html
<!DOCTYPE html>
<html lang="en">
<head>
<meta charset="utf-8">
<title>KVR Business Cards</title>
<link href="https://fonts.googleapis.com/css2?family=Montserrat:wght@400;500;600;700&display=swap" rel="stylesheet">
<style>
  :root{
    --bronze:#8f5f31;
    --ink:#1c1c1c;
    --paper:#ffffff;
    --stage:#c2c2c2;
  }
  *{box-sizing:border-box;margin:0;padding:0}
  html,body{width:1200px;height:788px;overflow:hidden}
  body{
    background:var(--stage);
    font-family:'Montserrat',Arial,sans-serif;
    display:flex;align-items:center;justify-content:center;gap:40px;
  }
  .card{
    position:relative;width:540px;height:310px;border-radius:22px;overflow:hidden;
    box-shadow:0 12px 30px rgba(0,0,0,.25);
  }

  /* Front */
  .card-front{background:var(--paper)}
  .front-band-dark{position:absolute;left:0;top:128px;width:330px;height:132px;background:var(--ink)}
  .front-band-step{position:absolute;left:330px;top:112px;width:40px;height:148px;background:var(--ink)}
  .front-band-bronze{position:absolute;right:0;top:0;width:118px;height:74px;background:var(--bronze)}
  .company{position:absolute;left:30px;top:52px}
  .company-name{font-weight:700;font-size:21px;letter-spacing:1px;color:var(--ink)}
  .company-tagline{font-weight:500;font-size:12.5px;letter-spacing:.6px;color:var(--bronze);margin-top:2px}
  .front-mark{position:absolute;left:392px;top:120px;display:flex;align-items:center;gap:10px}
  .mark-name{font-weight:600;font-size:46px;letter-spacing:3px;color:var(--bronze);line-height:1}
  .mark-square{width:14px;height:14px;background:var(--bronze)}
  .person{position:absolute;left:30px;top:146px}
  .person-name{font-weight:700;font-size:18px;letter-spacing:1.2px;color:var(--bronze)}
  .person-title{font-weight:500;font-size:11.5px;color:var(--paper);margin-top:2px}
  .contacts{list-style:none;margin-top:10px}
  .contacts li{display:flex;align-items:center;gap:8px;font-size:11.5px;color:var(--paper);margin-bottom:4px}
  .contacts svg{width:11px;height:11px;flex:none}
  .address{position:absolute;left:30px;top:276px;font-size:12px;font-weight:500;color:var(--ink);letter-spacing:.2px}

  /* Back */
  .card-back{background:var(--ink);color:var(--paper);text-align:center}
  .back-mark{position:absolute;left:0;right:0;top:44px;display:flex;align-items:center;justify-content:center;gap:10px}
  .back-mark .mark-name{font-size:42px}
  .back-company{position:absolute;left:0;right:0;top:112px}
  .back-company .company-name{color:var(--paper);font-size:20px}
  .back-company .company-tagline{font-size:12px}
  .services-head{position:absolute;left:34px;right:34px;top:182px;display:flex;align-items:center;gap:14px}
  .services-head .rule{flex:1;height:1px;background:var(--bronze)}
  .services-title{font-weight:700;font-size:15px;letter-spacing:1px;color:var(--bronze)}
  .services{position:absolute;left:0;right:0;top:216px;list-style:none;font-size:12.5px;font-weight:500;line-height:1.9}
  .services span{margin:0 8px;white-space:nowrap}
  .services span::before{content:"•";color:var(--bronze);margin-right:5px}
</style>
</head>
<body>

<article class="card card-front" aria-label="Business card front">
  <div class="front-band-dark"></div>
  <div class="front-band-step"></div>
  <div class="front-band-bronze"></div>

  <div class="company">
    <div class="company-name">KEVRA MANAGEMENT</div>
    <div class="company-tagline">Crafted to Keep Every Estate at Ease</div>
  </div>

  <div class="front-mark">
    <span class="mark-name">KVR</span>
    <span class="mark-square"></span>
  </div>

  <div class="person">
    <div class="person-name">DANIEL REYNOLD</div>
    <div class="person-title">Founder/CEO</div>
    <ul class="contacts">
      <li>
        <svg viewBox="0 0 12 12" aria-hidden="true"><path fill="var(--bronze)" d="M2.5 1l2 2-1 1.3c.6 1.3 1.6 2.3 2.9 2.9L7.7 6l2 2-1.2 1.6C5 9.3 2.4 6.7 1 3.2z"/></svg>
        (555)-214-3390
      </li>
      <li>
        <svg viewBox="0 0 12 12" aria-hidden="true"><rect x="1" y="2.5" width="10" height="7" fill="var(--bronze)"/><path d="M1 2.5l5 4 5-4" stroke="var(--ink)" stroke-width="1" fill="none"/></svg>
        info@kevramanagement.com
      </li>
      <li>
        <svg viewBox="0 0 12 12" aria-hidden="true"><circle cx="6" cy="6" r="5" fill="var(--bronze)"/><path d="M1 6h10M6 1c-2 3-2 7 0 10M6 1c2 3 2 7 0 10" stroke="var(--ink)" stroke-width=".8" fill="none"/></svg>
        www.kevramanagement.com
      </li>
    </ul>
  </div>

  <div class="address">1290 Harbor Crest Lane Northfield AB 2095</div>
</article>

<article class="card card-back" aria-label="Business card back">
  <div class="back-mark">
    <span class="mark-name">KVR</span>
    <span class="mark-square"></span>
  </div>
  <div class="back-company">
    <div class="company-name">KEVRA MANAGEMENT</div>
    <div class="company-tagline">Crafted to Keep Every Estate at Ease</div>
  </div>
  <div class="services-head">
    <span class="rule"></span>
    <span class="services-title">OUR SERVICES</span>
    <span class="rule"></span>
  </div>
  <p class="services">
    <span>Professional Property Management</span><span>Home Hosting &amp; Concierge</span><br>
    <span>Holliday Home / Income Property Management</span>
  </p>
</article>

</body>
</html>
```